Buch-/eBook-Cover für Sachbuch gesucht
Zielgruppe
We're selfpublishing nonfiction books. Interested are adults - mostly man (age range: 25-50) - who want to learn more about leadership at their workplaces.
Aufgabenstellung
The design should be clean and simple, title easy to read, good color contrast (the cover has to stand out from an white background).

```html
<!DOCTYPE html>
<html lang="en">
<head>
<meta charset="utf-8">
<title>Leadership – Book Cover</title>
<link rel="stylesheet" href="https://fonts.googleapis.com/css2?family=Barlow+Condensed:wght@600;700&family=Fira+Sans+Condensed:wght@600&display=swap">
<style>
  :root {
    --navy: #203a5e;
    --navy-deep: #1a3152;
    --navy-figures: #27456c;
    --light-yellow: #e8e07e;
    --cyan: #5cbfcc;
    --cyan-soft: #80c9d4;
    --magenta: #e1197d;
    --cream: #f4eee2;
  }
  html, body {
    margin: 0;
    padding: 0;
    width: 848px;
    height: 1200px;
    overflow: hidden;
    background: var(--navy);
  }
  .cover {
    display: block;
    width: 848px;
    height: 1200px;
  }
  .title-top {
    font-family: "Barlow Condensed", "Arial Narrow", sans-serif;
    font-weight: 600;
    fill: var(--cyan);
  }
  .title-bottom {
    font-family: "Barlow Condensed", "Arial Narrow", sans-serif;
    font-weight: 700;
    fill: var(--navy);
    stroke: var(--cream);
    stroke-width: 5;
    paint-order: stroke;
  }
  .subtitle {
    font-family: "Fira Sans Condensed", "Arial Narrow", sans-serif;
    font-weight: 600;
    fill: var(--magenta);
  }
  .subtitle-sticker { fill: var(--cream); }
  .author {
    font-family: "Fira Sans Condensed", "Arial Narrow", sans-serif;
    font-weight: 600;
    fill: var(--cyan-soft);
  }
</style>
</head>
<body>
<svg class="cover" viewBox="0 0 848 1200" xmlns="http://www.w3.org/2000/svg" role="img" aria-label="Leadership: Fostering Growth and Inspiring Excellence, by Daniel Hartley">
  <rect class="background" width="848" height="1200" fill="var(--navy)"/>
  <rect class="spine-edge" x="0" y="0" width="26" height="1200" fill="var(--navy-deep)"/>
  <polygon class="light-beam" points="28,0 848,0 848,965 341,885" fill="var(--light-yellow)"/>

  <text class="title-top" x="136" y="310" font-size="280" textLength="582" lengthAdjust="spacingAndGlyphs">LEADER</text>
  <text class="title-bottom" x="221" y="594" font-size="400" textLength="507" lengthAdjust="spacingAndGlyphs">SHIP</text>

  <g class="subtitle-block">
    <rect class="subtitle-sticker" x="130" y="628" width="522" height="86" rx="22"/>
    <rect class="subtitle-sticker" x="130" y="694" width="624" height="90" rx="22"/>
    <text class="subtitle" x="146" y="700" font-size="74" textLength="486" lengthAdjust="spacingAndGlyphs">Fostering Growth</text>
    <text class="subtitle" x="146" y="740" font-size="34" textLength="52" lengthAdjust="spacingAndGlyphs">and</text>
    <text class="subtitle" x="209" y="768" font-size="76" textLength="529" lengthAdjust="spacingAndGlyphs">Inspiring Excellence</text>
  </g>

  <rect class="walking-team" x="50" y="860" width="296" height="292" fill="var(--navy-figures)" role="img" aria-label="Small figures of people walking towards the light"/>

  <g class="author-name">
    <text class="author" x="341" y="1048" font-size="74" textLength="186" lengthAdjust="spacingAndGlyphs">Daniel</text>
    <text class="author" x="343" y="1104" font-size="74" textLength="184" lengthAdjust="spacingAndGlyphs">Hartley</text>
  </g>
</svg>
</body>
</html>
```